Mobile welding fabrication and repair, heavy equipment and semi repair

We need a business card design that will catch the eye but look prelesional at the same time. Were based out of Idaho and we do all welding fabrication jobs and repairs, we also build and install custom pipe fences for personal or larger scale fence jobs and can give free quotes. We can do semi truck and trailer repairs Mobily also.

Target Market(s)

Welding

Industry/Entity Type

welding and repair

Contact Information for Business Card

email (flintforgeandfix@mailvero.com, phone number 208-417-3862, owner (Wade Pellston), Pipe Fence, Semi Repair, Mobile welding and fabrication

Font styles to use
Sans Serif

Requirements
Must have
• My logo in black background on one side , and other side my logo in white back round with all the information listed on card details
Nice to have
• make it stand out from other business cards

```html
<!DOCTYPE html>
<html lang="en">
<head>
<meta charset="utf-8">
<title>Flint Forge and Fix – Business Card</title>
<link rel="stylesheet" href="https://fonts.googleapis.com/css2?family=Arimo:wght@400;700&display=swap">
<style>
  :root {
    --page: #ffffff;
    --card-white: #ffffff;
    --card-black: #000000;
    --brand-blue: #0b6dbf;
    --ink: #231f20;
    --muted: #8a8a8a;
    --tagline: #6f6f6f;
    --rule: #2f6fc4;
    --shadow: rgba(0,0,0,0.18);
  }
  * { margin: 0; padding: 0; box-sizing: border-box; }
  html, body {
    width: 1200px; height: 1200px; overflow: hidden;
    background: var(--page);
    font-family: "Arimo", Arial, sans-serif;
  }
  .canvas { position: relative; width: 1200px; height: 1200px; }
  .card {
    position: absolute; left: 294px; width: 612px; height: 382px; overflow: hidden;
  }
  .card--front {
    top: 205px; background: var(--card-white);
    box-shadow: 0 0 3px var(--shadow);
  }
  .card--back { top: 612px; background: var(--card-black); }

  .brand-name {
    color: var(--brand-blue); font-weight: 700; text-transform: uppercase;
    letter-spacing: 0.01em; line-height: 1;
  }
  .card--front .brand-name {
    position: absolute; left: 41px; top: 42px; font-size: 40px;
  }
  .card--front .brand-name span { display: block; font-size: 20px; margin-top: 8px; }

  .contact-block { position: absolute; left: 41px; top: 176px; }
  .person-name { font-size: 24px; font-weight: 700; color: var(--ink); letter-spacing: 0.01em; }
  .person-role { font-size: 19px; color: var(--muted); margin-top: 2px; }
  .contact-list { list-style: none; margin-top: 20px; }
  .contact-list li {
    display: flex; align-items: center; gap: 6px;
    font-size: 19px; color: var(--ink); line-height: 20px;
  }
  .contact-list svg { width: 14px; height: 15px; flex: none; }

  .divider {
    position: absolute; left: 277px; top: 309px; width: 58px; height: 2px; background: var(--rule);
  }
  .services {
    position: absolute; left: 0; right: 0; top: 322px; text-align: center;
    font-size: 16.5px; color: var(--tagline);
  }

  .card--back .brand-name {
    position: absolute; left: 0; right: 0; top: 130px; text-align: center; font-size: 64px;
  }
  .card--back .brand-name span { display: block; font-size: 30px; margin-top: 12px; }
</style>
</head>
<body>
<main class="canvas">
  <section class="card card--front" aria-label="Card front">
    <h1 class="brand-name">Flint Forge<span>and Fix</span></h1>

    <div class="contact-block">
      <p class="person-name">WADE PELLSTON</p>
      <p class="person-role">Owner</p>
      <ul class="contact-list">
        <li>
          <svg viewBox="0 0 14 15" aria-hidden="true"><rect x="3" y="1" width="8" height="13" rx="1.5" fill="none" stroke="#1a56b8" stroke-width="1.6"/><circle cx="7" cy="11.6" r="0.9" fill="#1a56b8"/></svg>
          208-417-3862
        </li>
        <li>
          <svg viewBox="0 0 14 15" aria-hidden="true"><path d="M1 6 L7 2 L13 6 V13 H1 Z" fill="#1a56b8"/><path d="M1 6 L7 10 L13 6 M1 13 L6 9 M13 13 L8 9" fill="none" stroke="#fff" stroke-width="1"/></svg>
          flintforgeandfix@mailvero.com
        </li>
      </ul>
    </div>

    <div class="divider"></div>
    <p class="services">Pipe Fence, Semi Repair, Mobile Welding and Fabrication</p>
  </section>

  <section class="card card--back" aria-label="Card back">
    <h2 class="brand-name">Flint Forge<span>and Fix</span></h2>
  </section>
</main>
</body>
</html>
```